依頼詳細
ラフ案を添付致しますのでそちらをベースにブラッシュアップお願いいたします。

お水の特徴は以下となります。
①分子が細かい(水分子のナノコロイダル化、六角形構造)
②浸透力が高い(脳細胞まで届くイメージ)
③科学的に研究された機能のある水

全体デザインは、上記イメージを踏まえてエネルギー溢れるようなデザインを希望致します。
記載項目
下部に記載する社名等はデザイン選定後にお伝えさせていただきます。
サイズ
A4
ページ数
片面
希望イメージ
シンプル 複雑
単色 カラフル
暗い 明るい
日常 高級
遊び心 厳粛
未来的 伝統的
女性的 男性的
希望する色
水色系
納品ファイル
• 高解像度JPG (.jpg)
• イラストレーター形式 (.ai)
• PNG形式 (.png)
補足説明
■ 選んだ理由

インパクトと躍動感のあるデザインだった為選ばせて頂きました。

■ 提案者全員のお礼・コメント

この度はたくさんのご提案誠にありがとうございます。
素敵なデザインが多く選定に悩ませて頂きました。
また機会がありましたらその際はどうぞよろしくお願い致します。

```html
<!DOCTYPE html>
<html lang="ja">
<head>
<meta charset="utf-8">
<title>高濃度シリカ水 OEM</title>
<link href="https://fonts.googleapis.com/css2?family=Noto+Sans+JP:wght@400;500;700;900&family=Zen+Maru+Gothic:wght@400;500;700&display=swap" rel="stylesheet">
<style>
  :root{
    --navy:#1b2f5a;
    --blue:#1f8fd6;
    --blue-deep:#0c6fb8;
    --sky:#cfeaf8;
    --sky-light:#eef8fd;
    --orange:#f28a1c;
    --orange-light:#f7a23a;
    --white:#ffffff;
    --text:#23324a;
  }
  *{margin:0;padding:0;box-sizing:border-box;}
  html,body{width:849px;height:1200px;overflow:hidden;background:var(--white);}
  body{font-family:"Noto Sans JP",sans-serif;color:var(--text);}
  .flyer{position:relative;width:849px;height:1200px;overflow:hidden;background:var(--white);}

  .water-backdrop{position:absolute;left:0;top:400px;width:849px;height:800px;
    background:linear-gradient(180deg,rgba(255,255,255,0) 0%,var(--sky) 20%,#b6def4 50%,#d9eff9 80%,var(--sky-light) 100%);}

  .lead{position:absolute;top:32px;left:0;width:100%;text-align:center;font-weight:700;font-size:26px;color:var(--navy);letter-spacing:1px;}
  .lead .mark{background:var(--blue);color:var(--white);padding:0 6px;margin:0 2px;}

  .headline{position:absolute;top:82px;left:0;width:100%;text-align:center;font-weight:900;font-size:100px;letter-spacing:2px;line-height:1.2;
    background:linear-gradient(180deg,#4fb3ea 0%,var(--blue-deep) 100%);-webkit-background-clip:text;background-clip:text;color:transparent;}

  .lot{position:absolute;top:232px;right:80px;font-weight:700;color:var(--navy);font-size:22px;white-space:nowrap;}
  .lot strong{font-size:34px;font-weight:900;}

  .bottle-photo{position:absolute;left:95px;top:215px;width:300px;height:320px;border-radius:8px;
    background:linear-gradient(160deg,#f4fbff 0%,#d5ecf8 60%,#bfe2f5 100%);}

  .badge{position:absolute;border-radius:50%;background:radial-gradient(circle at 35% 30%,var(--orange-light),var(--orange));
    color:var(--white);font-weight:700;display:flex;align-items:center;justify-content:center;text-align:center;line-height:1.3;
    box-shadow:0 3px 6px rgba(0,0,0,.12);}
  .badge-concentration{left:461px;top:352px;width:124px;height:124px;font-size:20px;}
  .badge-silica{left:610px;top:292px;width:140px;height:140px;font-size:18px;}
  .badge-science{left:504px;top:484px;width:124px;height:124px;font-size:19px;}
  .badge-size{left:660px;top:468px;width:124px;height:124px;font-size:20px;}

  .intro{position:absolute;top:612px;left:0;width:100%;text-align:center;font-weight:700;color:var(--navy);}
  .intro .sub{font-size:21px;}
  .intro .main{font-size:26px;font-weight:900;margin-top:4px;white-space:nowrap;}

  .pillar{position:absolute;top:696px;height:96px;font-family:"Zen Maru Gothic",sans-serif;color:var(--white);text-align:center;
    font-size:32px;line-height:1.3;font-weight:500;text-shadow:0 1px 4px rgba(12,111,184,.45);white-space:nowrap;}
  .pillar-silica{left:35px;width:355px;}
  .pillar-water{left:460px;width:355px;}
  .pillar svg{position:absolute;top:0;}
  .pillar .open{left:0;}
  .pillar .close{right:0;}
  .pillar .line{display:block;padding-top:2px;}
  .times{position:absolute;top:708px;left:395px;width:60px;text-align:center;font-size:64px;color:var(--white);font-weight:400;line-height:1;}

  .feature-list{position:absolute;left:70px;top:818px;width:330px;background:rgba(255,255,255,.9);padding:16px 20px;list-style:none;font-size:15px;line-height:1.45;color:var(--text);}
  .feature-list li{position:relative;padding-left:16px;margin-bottom:12px;}
  .feature-list li:last-child{margin-bottom:0;}
  .feature-list li::before{content:"";position:absolute;left:0;top:8px;width:7px;height:7px;background:var(--blue);border-radius:50%;}

  .molecule{position:absolute;top:824px;width:150px;height:100px;}
  .molecule-large{left:465px;}
  .molecule-small{left:640px;}
  .molecule .art{width:150px;height:90px;border-radius:4px;}
  .molecule-large .art{background:linear-gradient(135deg,#6fc0ec,#2a8fd0);}
  .molecule-small .art{background:linear-gradient(135deg,#9cd6f3,#4aa7dd);}
  .molecule .tag{position:absolute;top:-14px;left:-10px;width:38px;height:38px;border-radius:50%;background:var(--navy);color:var(--white);
    font-size:11px;font-weight:700;display:flex;align-items:center;justify-content:center;text-align:center;line-height:1.1;}
  .molecule .caption{text-align:center;font-size:12px;color:var(--navy);margin-top:3px;}

  .permeate{position:absolute;left:460px;top:936px;width:345px;text-align:center;color:var(--navy);}
  .permeate .sub{font-size:15px;font-weight:500;}
  .permeate .main{font-size:40px;font-weight:900;color:var(--blue-deep);letter-spacing:2px;line-height:1.2;}
</style>
</head>
<body>
<div class="flyer">
  <div class="water-backdrop" role="img" aria-label="水しぶきと水面の写真、淡い水色"></div>

  <p class="lead">話題のシリカ水を<span class="mark">自社ブランド</span>でつくりませんか?</p>
  <h1 class="headline">高濃度シリカ水</h1>
  <p class="lot">小ロット<strong>1,000</strong>本~</p>

  <div class="bottle-photo" role="img" aria-label="透明なペットボトル入りの水の写真"></div>

  <div class="badge badge-concentration">シリカ濃度<br>調整可</div>
  <div class="badge badge-silica">非晶質シリカ<br>水溶性ケイ素<br>clearo<br>配合</div>
  <div class="badge badge-science">科学的に<br>優れた<br>機能水</div>
  <div class="badge badge-size">選べる<br>サイズ</div>

  <div class="intro">
    <p class="sub">注目のミネラル「シリカ」とカラダに浸透しやすい機能水をブレンド</p>
    <p class="main">独自技術によってナノコロイダル化に成功した高濃度シリカ水</p>
  </div>

  <div class="pillar pillar-silica">
    <svg class="open" width="20" height="96" viewBox="0 0 20 96"><path d="M16 4 Q2 48 16 92" fill="none" stroke="#fff" stroke-width="2.5"/></svg>
    <span class="line">非晶質シリカ</span>
    <span class="line">水溶性ケイ素clearo</span>
    <svg class="close" width="20" height="96" viewBox="0 0 20 96"><path d="M4 4 Q18 48 4 92" fill="none" stroke="#fff" stroke-width="2.5"/></svg>
  </div>
  <div class="times">×</div>
  <div class="pillar pillar-water">
    <svg class="open" width="20" height="96" viewBox="0 0 20 96"><path d="M16 4 Q2 48 16 92" fill="none" stroke="#fff" stroke-width="2.5"/></svg>
    <span class="line">科学的に</span>
    <span class="line">優れた水機能水</span>
    <svg class="close" width="20" height="96" viewBox="0 0 20 96"><path d="M4 4 Q18 48 4 92" fill="none" stroke="#fff" stroke-width="2.5"/></svg>
  </div>

  <ul class="feature-list">
    <li>機能性、安全性エビデンスの充実<br>(ヒト臨床試験済、非臨床データ)</li>
    <li>アジアハラール認証原料</li>
    <li>シリカは鉱物由来、植物由来の<br>2種タイプから選択可能</li>
  </ul>

  <div class="molecule molecule-large">
    <div class="art" role="img" aria-label="大きな水分子の集まりの図"></div>
    <span class="tag">分子<br>大</span>
    <p class="caption">一般的な水</p>
  </div>
  <div class="molecule molecule-small">
    <div class="art" role="img" aria-label="細かい水分子の集まりの図"></div>
    <span class="tag">分子<br>小</span>
    <p class="caption">微細構造の水</p>
  </div>

  <div class="permeate">
    <p class="sub">微細分子＆活発な状態</p>
    <p class="main">浸透性が高い</p>
  </div>
</div>
</body>
</html>
```